Bootcamp Bikini Summer body 12 week challenge Flyer/Advertising

I require a 12 week summer challenge flyer/advertisements, of various sizes- A4, website banner, square instagram type.

The Details that must be on the advertisements:

Marla Pentwick presents the 'Get Summer ready' with her very own personalised programming to get you ultimate beach body- ready before Summer hits!
ONLY $59.95 per week
Includes:
-Customised meal plan (usually $220)
-Weekly weigh in/check ins with Marla!
-3 weekly training sessions, with different training style to ensure your body is always left guessing, in a fun team environment. Run by one of Marla's very own trainers, from Rise and Forge training facility!
-Discounted additional PT sessions.
-Qualified, experienced and result driven trainers
-Proven results with thousands of women, worldwide
-Prize pack for the challenge winner
-The best beach body ready for Summer!
SECURE YOUR PLACE NOW AS PLACES ARE CAPPED:
contact@marlapentwick.com.au or text 0491 586 307 to sign up NOW
(smaller writing)
t&c -Full 12 weeks must be paid for, even if sessions are missed or cancelled. Weekly deductions must be set up upon confirmation using a credit card, with the first 2 weeks deducted up front, the remaining 10 weeks will be deducted weekly.

```html
<!DOCTYPE html>
<html lang="en">
<head>
<meta charset="utf-8">
<title>Get Summer Ready – Marla Pentwick</title>
<link href="https://fonts.googleapis.com/css2?family=Open+Sans:ital,wght@0,400;0,600;0,700;1,800&display=swap" rel="stylesheet">
<style>
  :root{
    --pink:#e5337d;
    --pink-deep:#d81f6c;
    --pink-soft:#f7c9dc;
    --pink-pale:#fbe3ed;
    --ink:#3a2a30;
    --white:#ffffff;
  }
  *{margin:0;padding:0;box-sizing:border-box}
  html,body{width:851px;height:1200px;overflow:hidden;background:var(--white)}
  .flyer{
    position:relative;width:851px;height:1200px;overflow:hidden;
    font-family:"Open Sans",Arial,sans-serif;color:var(--ink);
    background:radial-gradient(circle at 75% 20%,#fdf1f6 0,var(--pink-pale) 45%,var(--pink-soft) 100%);
  }
  .hero-photo{
    position:absolute;left:420px;top:0;width:431px;height:935px;
    background:linear-gradient(180deg,#8a5a48 0%,#c98f74 30%,#e2b29b 55%,#d9a3a8 80%,rgba(247,201,220,0) 100%);
    border-radius:0 0 0 160px;opacity:.85;
  }
  .brand{
    position:absolute;left:113px;top:22px;width:200px;height:86px;background:var(--white);
    display:flex;align-items:center;justify-content:center;
    font-weight:700;font-size:38px;letter-spacing:3px;color:var(--pink);
  }
  .presents{position:absolute;left:128px;top:118px;font-size:24px;font-weight:600;color:var(--pink)}
  .headline{
    position:absolute;left:122px;top:148px;font-style:italic;font-weight:800;
    font-size:92px;line-height:80px;color:var(--pink);letter-spacing:-2px;
  }
  .intro{position:absolute;left:128px;top:398px;width:370px;font-size:24px;line-height:31px;font-weight:600}
  .price-badge{
    position:absolute;left:448px;top:420px;width:128px;height:128px;border-radius:50%;
    background:var(--pink);color:var(--white);text-align:center;
    display:flex;flex-direction:column;justify-content:center;
    box-shadow:0 4px 10px rgba(120,20,60,.25);transform:rotate(-8deg);
  }
  .price-badge .only{font-size:15px;font-weight:700}
  .price-badge .amount{font-size:34px;font-weight:800;font-style:italic;line-height:36px}
  .price-badge .per{font-size:15px;font-weight:600}
  .includes{position:absolute;left:128px;top:552px;width:400px;font-size:15.5px;line-height:21px}
  .includes h2{font-size:17px;font-weight:700;margin-bottom:4px}
  .includes li{list-style:none}
  .promo-photo{
    position:absolute;left:552px;top:800px;width:299px;height:165px;border:6px solid var(--white);
    background:linear-gradient(135deg,#f4eef0 0%,#e8d6d2 50%,#cfa58c 100%);
  }
  .footer-wave{position:absolute;left:0;top:900px;width:851px;height:300px}
  .cta{position:absolute;left:0;width:851px;top:1000px;text-align:center;color:var(--white)}
  .cta .secure{font-size:21px;font-weight:700;letter-spacing:.3px}
  .cta .contact{font-size:19px;font-weight:600;margin-top:4px}
  .terms{position:absolute;left:128px;width:600px;top:1078px;font-size:9.5px;line-height:13px;color:var(--white);text-align:left}
</style>
</head>
<body>
<div class="flyer">
  <div class="hero-photo" role="img" aria-label="Photo of a fit woman in sports top and shorts lifting dumbbells"></div>

  <div class="brand">MARLA</div>
  <p class="presents">presents the</p>
  <h1 class="headline">Get<br>Summer<br>ready</h1>

  <p class="intro">with her very own personalised programming to get you ultimate beach body- ready before Summer hits!</p>

  <div class="price-badge">
    <span class="only">ONLY</span>
    <span class="amount">$59.95</span>
    <span class="per">per week</span>
  </div>

  <section class="includes">
    <h2>Includes:</h2>
    <ul>
      <li>-Customised meal plan (usually $220)</li>
      <li>-Weekly weigh in/check ins with Marla!</li>
      <li>-3 weekly training sessions, with different training style to ensure your body is always left guessing, in a fun team environment. Run by one of Marla's very own trainers, from Rise and Forge training facility!</li>
      <li>-Discounted additional PT sessions.</li>
      <li>-Qualified, experienced and result driven trainers</li>
      <li>-Proven results with thousands of women, worldwide</li>
      <li>-Prize pack for the challenge winner</li>
      <li>-The best beach body ready for Summer!</li>
    </ul>
  </section>

  <div class="promo-photo" role="img" aria-label="Photo of a woman in a bikini doing a floor exercise"></div>

  <svg class="footer-wave" viewBox="0 0 851 300" preserveAspectRatio="none" aria-hidden="true">
    <path d="M0 70 C250 10 560 120 851 40 L851 300 L0 300 Z" fill="#f29bbf"/>
    <path d="M0 85 C260 30 570 135 851 60 L851 300 L0 300 Z" fill="var(--pink)"/>
  </svg>

  <div class="cta">
    <p class="secure">SECURE YOUR PLACE NOW AS PLACES ARE CAPPED:</p>
    <p class="contact">contact@marlapentwick.com.au or text 0491 586 307 to sign up NOW</p>
  </div>
  <p class="terms">t&amp;c -Full 12 weeks must be paid for, even if sessions are missed or cancelled. Weekly deductions must be set up upon confirmation using a credit card, with the first 2 weeks deducted up front, the remaining 10 weeks will be deducted weekly.</p>
</div>
</body>
</html>
```